Presentation Folder, Business Card, Letterhead and Envelope design

We are a dental clinic that will open in August and we are looking for a professional graphic designer to create our Business Card, Presentation Folder, Letterhead, Notepad and envelopes.

The brand NovaGrin must reflect a sense of quality and sophistication, marketed for middle-class consumers.
Our preference is for quality and refined materials, where less is more.
Attached the logo

```html
<!DOCTYPE html>
<html lang="en">
<head>
<meta charset="utf-8">
<title>NovaGrin Business Card</title>
<link rel="stylesheet" href="https://fonts.googleapis.com/css2?family=Montserrat:wght@300;400;600&family=Work+Sans:wght@400&display=swap">
<style>
  :root {
    --backdrop: #d2d3ce;
    --card-white: #ffffff;
    --brand-grey: #575757;
    --brand-red: #6b1012;
    --text-grey: #5a5a5a;
    --rule-red: #8c3a3a;
  }
  * { margin: 0; padding: 0; box-sizing: border-box; }
  html, body {
    width: 1200px; height: 1058px; overflow: hidden;
    background: var(--backdrop);
  }
  .stage {
    width: 1200px; height: 1058px;
    display: flex; flex-direction: column; align-items: center; justify-content: center;
    gap: 70px;
  }
  .card {
    width: 560px; height: 320px; position: relative;
    box-shadow: 0 12px 30px rgba(0,0,0,0.18);
  }
  .card-front { background: var(--card-white); display: flex; align-items: center; }
  .front-brand {
    width: 250px; display: flex; align-items: center; justify-content: center; gap: 12px;
  }
  .brand-square { width: 26px; height: 26px; background: var(--brand-red); }
  .front-brand .brand-name {
    font-family: 'Montserrat', sans-serif; font-weight: 600;
    font-size: 26px; color: var(--brand-grey); letter-spacing: 0.02em;
  }
  .divider { width: 1px; height: 150px; background: var(--rule-red); }
  .contact { padding-left: 34px; font-family: 'Work Sans', sans-serif; color: var(--text-grey); }
  .contact .person {
    font-family: 'Montserrat', sans-serif; font-weight: 600; font-size: 17px;
    color: var(--brand-red); letter-spacing: 0.02em;
  }
  .contact .role { font-size: 13px; margin-bottom: 14px; }
  .contact .address { font-size: 13px; line-height: 1.4; margin-bottom: 12px; }
  .contact .line { font-size: 13px; line-height: 1.45; display: flex; align-items: center; gap: 8px; }
  .contact svg { width: 10px; height: 10px; flex: none; }
  .card-back {
    background: var(--brand-grey);
    display: flex; align-items: center; justify-content: center; gap: 18px;
  }
  .back-square { width: 40px; height: 40px; background: var(--card-white); }
  .card-back .brand-name {
    font-family: 'Montserrat', sans-serif; font-weight: 300;
    font-size: 44px; color: var(--card-white); letter-spacing: 0.22em;
  }
</style>
</head>
<body>
<main class="stage">
  <section class="card card-front">
    <div class="front-brand">
      <span class="brand-square"></span>
      <span class="brand-name">NovaGrin</span>
    </div>
    <div class="divider"></div>
    <div class="contact">
      <p class="person">DANIEL ASHFORD</p>
      <p class="role">Director</p>
      <p class="address">418 Maple Crest Road<br>Springfield, IL 62704</p>
      <p class="line">
        <svg viewBox="0 0 10 10"><path d="M2 1 L4 1 L4.6 3 L3.4 4 Q4.5 6 6 6.6 L7 5.4 L9 6 L9 8 Q5 9 2 5 Q1 3 2 1Z" fill="var(--brand-red)"/></svg>
        +330 5512-0473
      </p>
      <p class="line">
        <svg viewBox="0 0 10 10"><rect x="0.7" y="2" width="8.6" height="6" fill="none" stroke="var(--brand-red)" stroke-width="1"/><path d="M0.7 2 L5 5.5 L9.3 2" fill="none" stroke="var(--brand-red)" stroke-width="1"/></svg>
        info@novagrin.com
      </p>
      <p class="line">
        <svg viewBox="0 0 10 10"><circle cx="5" cy="5" r="4.3" fill="none" stroke="var(--brand-red)" stroke-width="1"/><path d="M0.7 5 H9.3 M5 0.7 Q2.5 5 5 9.3 M5 0.7 Q7.5 5 5 9.3" fill="none" stroke="var(--brand-red)" stroke-width="0.8"/></svg>
        www.novagrin.com
      </p>
    </div>
  </section>
  <section class="card card-back">
    <span class="back-square"></span>
    <span class="brand-name">NOVAGRIN</span>
  </section>
</main>
</body>
</html>
```